B2B EDM Banner Design- Specialist Tech Company

We need a new top-of-email banner for our EDM campaigns for Varnel Brix (www.varnelbrix-example.com
). This banner will sit at the top of every email and must immediately signal the brand, look modern and professional, and be visually aligned with the tech/IT audience.
Size of the banner: Around 728x90 - it must fit at the top of an email blast.
Purpose of the Banner
Establish a strong, recognizable brand identity across all Varnel Brix EDMs
visually consistent with existing banners created for other brands (see reference examples provided)
Communicate Varnel Brix’s value proposition at a glance
Brand Name
Varnel Brix
Tagline (must appear in the banner)
“11,322 whitepapers from 726 companies”
Design Requirements
Style & Tone
Modern, clean, and professional
Tech-centric look and feel
High-quality, sleek, and corporate
Eye-catching but not cluttered
Should feel premium and authoritative
Layout & Composition
Full-width banner for email header
Horizontal orientation similar to the Plomtar and Quindle Staff Archive examples
Include space for the brand name/logo prominently on the left or centered
Integrate the tagline in a readable, secondary position
Optional: a subtle background texture or tech-related abstract pattern (circuitry, network nodes, gradient, etc.)
No busy imagery—should feel clean and trustworthy
Color Palette
Use colors consistent with Varnel Brix branding from www.varnelbrix-example.com
Blues, greys, blacks, and tech-style gradients preferred
Should feel consistent with a B2B IT audience
Typography
Clean, sans-serif fonts (professional/tech-aligned)
Brand name should be bold and prominent
Tagline should be smaller, but still readable on desktop and mobile
Imagery (if used)
Abstract tech shapes, network visuals, geometric patterns, or gradient overlays
Avoid photography of people
Keep imagery subtle so text remains legible
Call-to-Action Button (optional)
None required in this banner (unlike the HR examples)
Banner should remain a pure brand header
Deliverables
Final banner in PNG and JPG formats
2–3 design variations (if possible) for A/B testing
Dimensions optimized for EDM: ~600–700px wide (standard email width), proportionate height

```html
<!DOCTYPE html>
<html lang="en">
<head>
<meta charset="UTF-8">
<title>Varnel Brix – Email Header Banner</title>
<link href="https://fonts.googleapis.com/css2?family=Montserrat:ital,wght@0,400;0,700;0,800;1,700;1,800&display=swap" rel="stylesheet">
<style>
  :root {
    --navy-deep: #03061a;
    --navy: #060f33;
    --blue-mid: #0a2a7a;
    --blue-bright: #1457d6;
    --cyan: #29a8e8;
    --white: #ffffff;
  }
  html, body {
    margin: 0;
    padding: 0;
    width: 1200px;
    height: 149px;
    overflow: hidden;
    background: var(--navy-deep);
  }
  .banner {
    position: relative;
    width: 1200px;
    height: 149px;
    overflow: hidden;
    font-family: "Montserrat", sans-serif;
    color: var(--white);
    background: linear-gradient(90deg, var(--navy-deep) 0%, #050a24 40%, var(--navy) 60%, var(--blue-mid) 82%, #0b3ca8 100%);
  }
  .banner__tech-visual {
    position: absolute;
    top: 0;
    right: 0;
    width: 400px;
    height: 149px;
    background:
      radial-gradient(ellipse at 62% 70%, rgba(120, 210, 255, 0.55) 0%, rgba(40, 130, 240, 0.25) 28%, rgba(20, 80, 200, 0) 60%),
      linear-gradient(90deg, rgba(10, 40, 120, 0) 0%, rgba(20, 90, 220, 0.45) 55%, rgba(25, 110, 235, 0.6) 100%);
  }
  .brand {
    position: absolute;
    left: 62px;
    top: 37px;
    display: flex;
    align-items: center;
  }
  .brand__mark {
    width: 74px;
    height: 74px;
    border-radius: 50%;
    background: var(--cyan);
    flex: none;
  }
  .brand__text {
    margin-left: 30px;
  }
  .brand__name {
    font-weight: 800;
    font-size: 41px;
    line-height: 1;
    letter-spacing: 0.5px;
    text-transform: uppercase;
    white-space: nowrap;
    width: 300px;
  }
  .brand__rule {
    width: 300px;
    height: 2px;
    background: var(--cyan);
    margin: 7px 0 5px;
  }
  .brand__tagline {
    font-weight: 700;
    font-size: 12px;
    letter-spacing: 9.6px;
    text-transform: uppercase;
    white-space: nowrap;
  }
  .offer {
    position: absolute;
    left: 542px;
    top: 42px;
  }
  .offer__headline {
    margin: 0;
    font-style: italic;
    font-weight: 800;
    font-size: 29px;
    line-height: 1;
    letter-spacing: 0.2px;
  }
  .offer__sub {
    margin: 9px 0 0;
    font-weight: 400;
    font-size: 19px;
    line-height: 1;
  }
</style>
</head>
<body>
  <header class="banner">
    <div class="banner__tech-visual" role="img" aria-label="Abstract glowing blue server towers on a circuit board network"></div>

    <div class="brand">
      <div class="brand__mark"></div>
      <div class="brand__text">
        <div class="brand__name">Varnel Brix</div>
        <div class="brand__rule"></div>
        <div class="brand__tagline">For IT Professionals</div>
      </div>
    </div>

    <div class="offer">
      <p class="offer__headline">11,322 whitepapers</p>
      <p class="offer__sub">from 726 companies</p>
    </div>
  </header>
</body>
</html>
```